Gulfvane Cooling LLC

we need a business card design

Industry/Entity Type

hvac

Contact Information for Business Card

my logo

Requirements
Must have
• my logo and same colors

```html
<!DOCTYPE html>
<html lang="en">
<head>
<meta charset="utf-8">
<title>Gulfvane Cooling LLC – Business Card</title>
<link rel="stylesheet" href="https://fonts.googleapis.com/css2?family=Rubik:wght@400;500;700&family=Saira+Condensed:wght@800&display=swap">
<style>
  :root {
    --backdrop: #3d3a4b;
    --brand-blue: #0a5db5;
    --brand-blue-light: #0b79d6;
    --brand-navy: #123f7c;
    --accent-orange: #f4b23e;
    --card-white: #ffffff;
    --card-mist: #e8edf2;
    --ink: #2b3340;
  }
  * { margin: 0; padding: 0; box-sizing: border-box; }
  html, body { width: 1200px; height: 789px; overflow: hidden; }
  body {
    background: var(--backdrop);
    font-family: "Rubik", sans-serif;
    position: relative;
  }
  .card {
    position: absolute;
    top: 240px;
    width: 540px;
    height: 309px;
    border-radius: 20px;
    overflow: hidden;
  }
  .card--front {
    left: 40px;
    background: linear-gradient(160deg, var(--card-white) 40%, var(--card-mist));
  }
  .card--back {
    left: 620px;
    background: radial-gradient(circle at 30% 25%, var(--brand-blue-light), var(--brand-blue) 70%);
    display: flex;
    align-items: center;
    justify-content: center;
  }
  .card__shapes { position: absolute; inset: 0; }
  .holder {
    position: absolute;
    left: 262px;
    top: 42px;
    color: var(--card-white);
  }
  .holder__name {
    font-family: "Saira Condensed", sans-serif;
    font-weight: 800;
    font-size: 36px;
    line-height: 1;
    letter-spacing: 0.5px;
  }
  .holder__role { font-size: 13px; margin-top: 4px; }
  .brand {
    position: absolute;
    display: flex;
    align-items: center;
    gap: 10px;
    font-family: "Rubik", sans-serif;
    font-weight: 700;
    line-height: 1.1;
  }
  .brand__dot { border-radius: 50%; flex: none; }
  .card--front .brand { left: 30px; top: 110px; color: var(--brand-navy); font-size: 19px; }
  .card--front .brand__dot { width: 34px; height: 34px; background: var(--accent-orange); }
  .card--back .brand { position: static; color: var(--card-white); font-size: 30px; }
  .card--back .brand__dot { width: 50px; height: 50px; background: var(--accent-orange); }
  .contacts {
    position: absolute;
    left: 30px;
    bottom: 30px;
    list-style: none;
    font-size: 12.5px;
    color: var(--ink);
  }
  .contacts li { display: flex; align-items: center; gap: 10px; margin-top: 6px; }
  .contacts svg { width: 13px; height: 13px; fill: var(--brand-blue); flex: none; }
  .socials {
    position: absolute;
    right: 40px;
    top: 172px;
    list-style: none;
    font-size: 13px;
    color: var(--ink);
  }
  .socials li { display: flex; align-items: center; gap: 10px; margin-top: 8px; }
  .socials__mark { width: 12px; height: 12px; border-radius: 50%; background: var(--brand-blue); flex: none; }
</style>
</head>
<body>
  <section class="card card--front">
    <svg class="card__shapes" viewBox="0 0 540 309" preserveAspectRatio="none" aria-hidden="true">
      <path d="M238 0 H540 V118 C460 122 360 135 296 158 C262 170 240 150 236 110 Z" fill="var(--brand-navy)" opacity="0.25" transform="translate(0 8)"/>
      <path d="M238 0 H540 V112 C460 118 360 130 296 150 C262 162 240 142 236 104 Z" fill="var(--accent-orange)" transform="translate(0 8)"/>
      <path d="M238 0 H540 V112 C460 118 360 130 296 150 C262 162 240 142 236 104 Z" fill="var(--brand-blue)"/>
      <path d="M300 309 C400 300 480 270 540 240 V309 Z" fill="var(--accent-orange)"/>
      <path d="M290 309 C400 296 480 268 540 236 V244 C480 276 400 302 310 309 Z" fill="var(--card-white)"/>
    </svg>
    <div class="holder">
      <div class="holder__name">DANA WHITLOW</div>
      <div class="holder__role">Managing Director</div>
    </div>
    <div class="brand"><span class="brand__dot"></span><span>Gulfvane<br>Cooling LLC</span></div>
    <ul class="contacts">
      <li><svg viewBox="0 0 24 24"><path d="M6.6 10.8a15 15 0 0 0 6.6 6.6l2.2-2.2a1 1 0 0 1 1-.25 11.4 11.4 0 0 0 3.6.57 1 1 0 0 1 1 1V20a1 1 0 0 1-1 1A17 17 0 0 1 3 4a1 1 0 0 1 1-1h3.5a1 1 0 0 1 1 1c0 1.25.2 2.45.57 3.57a1 1 0 0 1-.25 1z"/></svg>+1 727-555-0148</li>
      <li><svg viewBox="0 0 24 24"><path d="M12 2a7 7 0 0 0-7 7c0 5.2 7 13 7 13s7-7.8 7-13a7 7 0 0 0-7-7zm0 9.5A2.5 2.5 0 1 1 12 6.5a2.5 2.5 0 0 1 0 5z"/></svg>Seabreeze, FL, United States, 33700</li>
      <li><svg viewBox="0 0 24 24"><path d="M2 5h20v14H2z M2 5l10 8 10-8" fill="var(--brand-blue)"/><path d="M3 6l9 7 9-7" fill="none" stroke="#fff" stroke-width="1.6"/></svg>dana@gulfvanecooling.com</li>
      <li><svg viewBox="0 0 24 24"><circle cx="12" cy="12" r="10"/><path d="M2 12h20M12 2c3 3 3 17 0 20M12 2c-3 3-3 17 0 20" fill="none" stroke="#fff" stroke-width="1.4"/></svg>www.gulfvanecooling.com</li>
    </ul>
    <ul class="socials">
      <li><span class="socials__mark"></span>gulfvanecooling</li>
      <li><span class="socials__mark"></span>gulfvanecooling</li>
    </ul>
  </section>

  <section class="card card--back">
    <div class="brand"><span class="brand__dot"></span><span>Gulfvane<br>Cooling LLC</span></div>
  </section>
</body>
</html>
```